Homebuilder & Remodeling Firm looking for archectrual looking website

We are a Custom home building & remodeling company since 1986 and would like to launch a website.Tom Halvery the principle of the firm is a graduate of Marlow Univesity school of architecture and draws his own designs and working drawings. and has done many residential, single and multi family projects in the Dallas Ft Worth Metroplex. We want our website to be architectural in design and visually appealing. We will eventually have photos to provide for you. The message we want to communicate is we have current update knowledge with trends, and longevity in experience. Our message is that we are a firm that designs and remodels fully through and we provide a well executed custom home that is unique to each client. The Homes that we build are unique ,authentic and sustainable architectural styles such as mid century modern, contemporary, transitional and they are sophisticated homes to compliment individual lifestyles of our clients. We have a passion for construction and an attention to detail that makes your dreams come to life. We listen to each clients every need in functionality and form and take them from pre-construction to post-construction follow -up.
We help you invest in your home. Thoughts Create Reality

EXAMPLES OF WEBSITES THAT WE LIKE. PLEASE DO
MORE CONTEMPORARY, SLEEK, ARCHITECTURAL

* Please make the LOGO a bigger part of design

http://penwickgroup.build/
https://www.quillorn.co/
http://vantrelmodernhomes.com/
http://www.neilcorradesign.com/
http://www.fennickolde.com/
http://ravodesignstudios.com/about
http://mendaleigc.com/

thank you,

Reason: We have many clients asking to see our website and re ready to launch something for them to look at

Target Market(s)

Home owners, home buyers, interior designers, All ages

Industry/Entity Type

Builders

Coding

Coded - Design and coding required

Number of Pages Required

5+ page

Font styles to use
Sans Serif

Requirements
Must have
• HTML5 OR PHP
• graphic artist must speak English:
• *Visually appealing, user friendly,
• * the website should reflect the stability and integrity of the company since it has been in business for over 30 years
• * a sophistication and refinement is our mandate.
Should not have
• Too busy, too much going on, we want more minimal in design and artsitic

```html
<!DOCTYPE html>
<html lang="en">
<head>
<meta charset="utf-8">
<title>Halvery Development — Custom Homes &amp; Remodeling</title>
<link href="https://fonts.googleapis.com/css2?family=Jost:wght@400;500;600&family=Open+Sans:wght@400;600&display=swap" rel="stylesheet">
<style>
:root{
  --blue:#114c91;
  --blue-dark:#0c3a70;
  --ink:#2a2a2a;
  --muted:#555b63;
  --grey:#9fa3a8;
  --panel:#ebecef;
  --field:#ececee;
  --white:#ffffff;
  --line:#d8dadf;
  --quote:#e3e4e7;
}
*{box-sizing:border-box;margin:0;padding:0}
html,body{width:1200px;height:3435px;overflow:hidden;background:var(--white)}
body{position:relative;font-family:"Open Sans",Arial,sans-serif;color:var(--ink)}
.abs{position:absolute}
.heading{font-family:"Jost",Arial,sans-serif;font-weight:600;color:var(--blue);text-transform:uppercase}

/* hero */
.hero{left:0;top:0;width:1200px;height:683px;background:linear-gradient(180deg,#5c93d6 0%,#8fb5dd 30%,#6b7684 55%,#4f6a3b 80%,#6f9a3c 100%)}
.hero-arrow{top:326px;width:38px;height:44px;background:rgba(0,0,0,.75);display:flex;align-items:center;justify-content:center}
.hero-label{left:130px;top:543px;width:436px;height:137px;background:rgba(17,76,145,.82);padding:20px 34px;font-family:"Jost",sans-serif;font-weight:500;font-size:44px;line-height:50px;color:var(--white);text-transform:uppercase;white-space:nowrap}

/* header */
.header{left:126px;top:0;width:955px;height:126px;background:var(--white);box-shadow:0 2px 10px rgba(0,0,0,.15)}
.brand{left:22px;top:30px;display:flex;align-items:center;gap:14px}
.brand-square{width:56px;height:56px;background:var(--blue)}
.brand-name{font-family:"Jost",sans-serif;font-weight:500;font-size:31px;line-height:34px;color:var(--blue);white-space:nowrap}
.brand-tag{font-family:"Jost",sans-serif;font-size:12px;letter-spacing:4px;color:var(--grey);text-transform:uppercase;white-space:nowrap}
.call{left:468px;top:24px;display:flex;align-items:center;gap:10px;font-size:11px;color:var(--ink);white-space:nowrap}
.call-icon{width:28px;height:28px;border:1px solid var(--blue);display:flex;align-items:center;justify-content:center}
.call strong{font-family:"Jost",sans-serif;font-weight:500;font-size:20px;color:var(--blue)}
.quote{left:784px;top:16px;width:140px;height:40px;background:var(--blue);color:var(--white);font-family:"Jost",sans-serif;font-size:12px;font-weight:500;display:flex;align-items:center;justify-content:center;gap:8px;white-space:nowrap}
.nav{left:468px;top:80px;display:flex;font-family:"Jost",sans-serif;font-size:12px;text-transform:uppercase;white-space:nowrap}
.nav span{padding:7px 11px;margin-right:18px;color:var(--ink)}
.nav span:last-child{margin-right:0}
.nav .active{background:var(--blue);color:var(--white)}

/* welcome */
.welcome{left:0;top:683px;width:1200px;height:497px;box-shadow:0 6px 10px rgba(0,0,0,.06)}
.eyebrow{left:0;top:50px;width:1200px;text-align:center;font-family:"Jost",sans-serif;font-size:14px;letter-spacing:3px;color:var(--muted)}
.intro{left:260px;top:82px;width:680px;text-align:center;font-size:19px;line-height:33px;color:var(--ink)}
.feature{top:190px;width:300px;text-align:center}
.feature svg{display:block;margin:0 auto}
.feature h3{margin-top:34px;font-family:"Jost",sans-serif;font-weight:500;font-size:15px;color:var(--blue);text-transform:uppercase}
.feature p{margin-top:18px;font-size:11.5px;line-height:22px;color:var(--ink)}
.btn-outline{display:inline-block;margin-top:20px;padding:8px 24px;border:1px solid var(--blue);border-radius:20px;font-family:"Jost",sans-serif;font-size:10.5px;color:var(--blue);text-transform:uppercase}

/* services */
.section-title{left:0;width:1200px;text-align:center;font-size:30px}
.title-rule{height:2px;background:var(--grey)}
.service{top:1347px;width:295px;height:277px;display:flex;align-items:center;justify-content:center}
.service-tag{border:2px solid rgba(255,255,255,.9);padding:8px 12px;font-family:"Jost",sans-serif;font-weight:500;font-size:16px;color:var(--white);text-transform:uppercase;background:rgba(0,0,0,.18);white-space:nowrap}

/* why choose */
.why{left:0;top:1680px;width:1200px;height:558px;background:var(--panel)}
.why h2{left:133px;top:50px;font-size:30px}
.why-lead{left:133px;top:132px;width:470px;font-size:13px;line-height:27px;color:var(--ink)}
.reason{left:133px;display:flex;align-items:center;gap:22px}
.reason-icon{width:60px;height:60px;border:1.5px solid var(--blue);border-radius:50%;display:flex;align-items:center;justify-content:center;background:var(--white)}
.reason h4{font-family:"Jost",sans-serif;font-weight:500;font-size:15px;color:var(--blue);text-transform:uppercase}
.reason p{margin-top:8px;font-size:11px;color:var(--ink)}
.why-divider{left:683px;top:60px;width:1px;height:430px;background:var(--line)}
.why-mark{left:780px;top:170px;width:300px;text-align:center;font-family:"Jost",sans-serif;font-weight:600;font-size:44px;line-height:54px;color:var(--blue)}
.why-mark-square{display:block;margin:0 auto 26px;width:120px;height:120px;background:var(--blue)}

/* testimonials */
.testi-title{left:131px;top:2293px;font-size:30px}
.testi-arrow{top:2328px;width:36px;height:36px;border-radius:50%;background:var(--blue);display:flex;align-items:center;justify-content:center}
.testi-card{top:2402px;height:271px;background:var(--white);border:1px solid var(--line);box-shadow:0 3px 10px rgba(0,0,0,.08);padding:68px 56px 0}
.testi-card p{position:relative;z-index:1;font-size:14px;line-height:28px;color:var(--ink);text-align:justify}
.quote-mark{z-index:0;font-family:"Jost",sans-serif;font-size:110px;line-height:1;height:60px;overflow:hidden;color:var(--quote)}
.author{position:absolute;z-index:1;display:flex;align-items:center;gap:10px}
.avatar{width:40px;height:40px;border-radius:50%;background:#b9b1a8}
.author b{display:block;font-family:"Jost",sans-serif;font-weight:500;font-size:10px;color:var(--blue);text-transform:uppercase}
.author span{font-size:10px;color:var(--ink)}

/* promo banners */
.promo{top:2740px;width:600px;height:300px;text-align:center;color:var(--white);padding-top:80px}
.promo h3{font-family:"Jost",sans-serif;font-weight:500;font-size:27px;text-transform:uppercase}
.promo p{margin-top:2px;font-size:18px}
.btn-light{display:inline-block;margin-top:24px;padding:10px 30px;border:2px solid var(--white);border-radius:24px;font-family:"Jost",sans-serif;font-size:11px;text-transform:uppercase}

/* footer */
.footer-brand{left:145px;top:3114px;display:flex;align-items:center;gap:14px}
.footer-rule{left:127px;top:3210px;width:430px;height:1px;background:var(--line)}
.follow{left:217px;top:3253px;display:flex;align-items:center;gap:8px;font-family:"Jost",sans-serif;font-size:11px;color:var(--blue);text-transform:uppercase;white-space:nowrap}
.social{width:28px;height:28px;border-radius:50%}
.footer-divider{left:600px;top:3040px;width:1px;height:297px;background:var(--line)}
.consult{left:645px;top:3078px;font-size:15px;font-family:"Jost",sans-serif}
.field{height:44px;border-radius:22px;background:var(--field);padding:0 20px;display:flex;align-items:center;justify-content:space-between;font-size:10.5px;color:var(--ink)}
.book{left:950px;top:3255px;width:116px;height:42px;border-radius:21px;background:var(--blue);color:var(--white);font-family:"Jost",sans-serif;font-weight:500;font-size:12px;display:flex;align-items:center;justify-content:center;text-transform:uppercase}
.bottom{left:0;top:3337px;width:1200px;height:98px;border-top:1px solid var(--line)}
.bottom-nav{left:131px;top:42px;font-size:9.5px;color:var(--ink);text-transform:uppercase}
.bottom-nav i{font-style:normal;margin:0 8px;color:var(--grey)}
.copyright{right:135px;top:42px;font-size:9.5px;color:var(--ink)}
</style>
</head>
<body>

<section class="abs hero" role="img" aria-label="Photo of a large custom two-storey home with gabled roofs, landscaped lawn and blue sky"></section>
<div class="abs hero-arrow" style="left:0"><svg width="12" height="18"><path d="M9 2 3 9l6 7" fill="none" stroke="#fff" stroke-width="2"/></svg></div>
<div class="abs hero-arrow" style="left:1162px"><svg width="12" height="18"><path d="M3 2l6 7-6 7" fill="none" stroke="#fff" stroke-width="2"/></svg></div>
<div class="abs hero-label">Custom<br>Home Building</div>

<header class="abs header">
  <div class="abs brand">
    <span class="brand-square"></span>
    <div><div class="brand-name">Halvery Development</div><div class="brand-tag">Custom Homes · Remodeling</div></div>
  </div>
  <div class="abs call">
    <span class="call-icon"><svg width="14" height="14" viewBox="0 0 24 24"><path d="M6.6 10.8a15 15 0 0 0 6.6 6.6l2.2-2.2a1 1 0 0 1 1-.25 11 11 0 0 0 3.6.6 1 1 0 0 1 1 1V20a1 1 0 0 1-1 1A17 17 0 0 1 3 4a1 1 0 0 1 1-1h3.5a1 1 0 0 1 1 1 11 11 0 0 0 .6 3.6 1 1 0 0 1-.25 1z" fill="#114c91"/></svg></span>
    CALL US : <strong>(888).888.8888</strong>
  </div>
  <div class="abs quote"><svg width="12" height="12" viewBox="0 0 24 24"><path d="M3 17.2V21h3.8L17.8 9.9l-3.8-3.8zM20.7 7a1 1 0 0 0 0-1.4l-2.3-2.3a1 1 0 0 0-1.4 0l-1.8 1.8 3.8 3.8z" fill="#fff"/></svg>GET A QUOTE</div>
  <nav class="abs nav"><span class="active">Home</span><span>About Us</span><span>Services</span><span>Testimonials</span><span>Contact Us</span></nav>
</header>

<section class="abs welcome">
  <div class="abs eyebrow">WELCOME TO OUR SITE</div>
  <p class="abs intro">There are many variations of passages of Lorem Ipsum available, but the majority have suffered alteration in some form, by injected</p>

  <div class="abs feature" style="left:115px">
    <svg width="70" height="60" viewBox="0 0 70 60" fill="none" stroke="#114c91" stroke-width="2"><path d="M4 28 35 6l31 22"/><path d="M12 24v30h46V24"/><rect x="20" y="34" width="12" height="20"/><rect x="40" y="34" width="12" height="10"/><path d="M2 56h66"/></svg>
    <h3>New Homes</h3>
    <p>It is a long established fact that a reader will be distracted by the readable content.</p>
    <span class="btn-outline">Learn More</span>
  </div>
  <div class="abs feature" style="left:450px">
    <svg width="70" height="60" viewBox="0 0 70 60" fill="none" stroke="#114c91" stroke-width="2"><path d="M14 6 60 52l-10 4 4-10L8 0z" transform="translate(2 2)"/><path d="M10 46 46 10l10 10-36 36H10z"/><path d="M18 38l4 4M26 30l4 4M34 22l4 4"/></svg>
    <h3>Custom Design Gallery</h3>
    <p>It is a long established fact that a reader will be distracted by the readable content.</p>
    <span class="btn-outline">Get Inspired</span>
  </div>
  <div class="abs feature" style="left:785px">
    <svg width="70" height="60" viewBox="0 0 70 60" fill="none" stroke="#114c91" stroke-width="2"><path d="M14 56V22h22v34M36 30h18v26"/><path d="M10 56h52"/><path d="M40 4v14M40 4h24M58 4v8"/><path d="M20 28h4M28 28h4M20 36h4M28 36h4M20 44h4M28 44h4M42 38h4M48 38h4M42 46h4M48 46h4"/></svg>
    <h3>Remodeling</h3>
    <p>It is a long established fact that a reader will be distracted by the readable content.</p>
    <span class="btn-outline">See Our Work</span>
  </div>
</section>

<h2 class="abs heading section-title" style="top:1232px">Our Services</h2>
<div class="abs title-rule" style="left:555px;top:1295px;width:90px"></div>

<div class="abs service" style="left:133px;background:linear-gradient(180deg,#7d93aa,#4e5f70 60%,#5f8a3d)" role="img" aria-label="Photo of a completed custom home with a front garden path"><span class="service-tag">Custom Home Building</span></div>
<div class="abs service" style="left:453px;background:linear-gradient(180deg,#7aa8d6,#8a7560 55%,#3a8ab8)" role="img" aria-label="Photo of a house under remodeling with scaffolding beside a pool"><span class="service-tag">Remodeling</span></div>
<div class="abs service" style="left:772px;background:linear-gradient(180deg,#4b3627,#a8683a 55%,#6b3f22)" role="img" aria-label="Photo of a new kitchen room addition with wood floors"><span class="service-tag">Home &amp; Room Additions</span></div>

<section class="abs why">
  <h2 class="abs heading">Why Choose Us</h2>
  <div class="abs title-rule" style="left:133px;top:98px;width:60px;background:var(--blue)"></div>
  <p class="abs why-lead">There are many variations of passages of Lorem Ipsum available, but the have suffered alteration in some form, by injected humour.</p>

  <div class="abs reason" style="top:220px">
    <span class="reason-icon"><svg width="28" height="28" viewBox="0 0 28 28" fill="#114c91"><circle cx="14" cy="8" r="5"/><path d="M4 26c0-6 4.5-10 10-10s10 4 10 10z"/></svg></span>
    <div><h4>We Are Profesional</h4><p>There are many variations of passages of Lorem</p></div>
  </div>
  <div class="abs reason" style="top:321px">
    <span class="reason-icon"><svg width="28" height="28" viewBox="0 0 28 28"><circle cx="14" cy="14" r="11" fill="#114c91"/><path d="M9 14l3.5 3.5L19 10" fill="none" stroke="#fff" stroke-width="2.4"/></svg></span>
    <div><h4>Quality Work</h4><p>There are many variations of passages of Lorem</p></div>
  </div>
  <div class="abs reason" style="top:422px">
    <span class="reason-icon"><svg width="30" height="28" viewBox="0 0 30 28" fill="#114c91"><circle cx="8" cy="9" r="3.5"/><circle cx="15" cy="7" r="4"/><circle cx="22" cy="9" r="3.5"/><path d="M2 24c0-5 3-8 6-8s6 3 6 8zM16 24c0-5 3-8 6-8s6 3 6 8zM8 24c0-6 3-10 7-10s7 4 7 10z"/></svg></span>
    <div><h4>Team</h4><p>There are many variations of passages of Lorem</p></div>
  </div>

  <div class="abs why-divider"></div>
  <div class="abs why-mark"><span class="why-mark-square"></span>Halvery<br>Development</div>
</section>

<h2 class="abs heading testi-title">Testimonials</h2>
<div class="abs title-rule" style="left:131px;top:2352px;width:60px;background:var(--blue)"></div>
<div class="abs testi-arrow" style="left:980px"><svg width="10" height="14"><path d="M7 2 2 7l5 5" fill="none" stroke="#fff" stroke-width="2"/></svg></div>
<div class="abs testi-arrow" style="left:1029px"><svg width="10" height="14"><path d="M3 2l5 5-5 5" fill="none" stroke="#fff" stroke-width="2"/></svg></div>

<article class="abs testi-card" style="left:133px;width:456px">
  <span class="abs quote-mark" style="left:20px;top:8px">“</span>
  <span class="abs quote-mark" style="left:160px;top:196px">”</span>
  <p>There are many variations of passages of Lorem Ipsum available, but the majority have suffered alteration in some form, by Injected humour, or randomised words which going.</p>
  <div class="author" style="left:250px;top:210px"><span class="avatar" role="img" aria-label="Client portrait"></span><div><b>Daniel Corvet</b><span>Australia</span></div></div>
</article>
<article class="abs testi-card" style="left:609px;width:458px">
  <span class="abs quote-mark" style="left:20px;top:8px">“</span>
  <span class="abs quote-mark" style="left:250px;top:196px">”</span>
  <p>It is a long established fact that a reader will be distracted by the readable content of a page when looking at its layout. The point of using Lorem Ipsum is that it has a more-or-less normal.</p>
  <div class="author" style="left:310px;top:210px"><span class="avatar" role="img" aria-label="Client portrait"></span><div><b>Milo Brant</b><span>Australia</span></div></div>
</article>

<section class="abs promo" style="left:0;background:linear-gradient(180deg,#3a4e6c,#55606a 55%,#3e4a3a)" role="img" aria-label="Photo of a remodeled two-storey house with garage">
  <h3>Remodeling Portfolio</h3><p>There are many variations of passages</p><span class="btn-light">Learn More</span>
</section>
<section class="abs promo" style="left:600px;background:linear-gradient(180deg,#1d3556,#4a4d55 50%,#b07a3e 80%,#2c4a66)" role="img" aria-label="Photo of a lit custom home at dusk with a pool">
  <h3>Custom Home Delivery</h3><p>There are many variations of passages</p><span class="btn-light">Learn More</span>
</section>

<div class="abs footer-brand">
  <span class="brand-square" style="width:58px;height:58px"></span>
  <div><div class="brand-name">Halvery Development</div><div class="brand-tag">Custom Homes · Remodeling</div></div>
</div>
<div class="abs footer-rule"></div>
<div class="abs follow">Follow Us :
  <span class="social" style="background:#3b5a9a"></span>
  <span class="social" style="background:#2a9fe0"></span>
  <span class="social" style="background:#46608f"></span>
  <span class="social" style="background:#dd5a3c"></span>
</div>
<div class="abs footer-divider"></div>
<div class="abs heading consult">Free Consultation</div>
<div class="abs field" style="left:645px;top:3127px;width:203px">Name</div>
<div class="abs field" style="left:862px;top:3127px;width:205px">E-mail</div>
<div class="abs field" style="left:645px;top:3185px;width:203px">Phone No.</div>
<div class="abs field" style="left:862px;top:3185px;width:205px">Type of Project <svg width="10" height="6"><path d="M0 0h10L5 6z" fill="#2a2a2a"/></svg></div>
<div class="abs book">Book Now</div>

<footer class="abs bottom">
  <div class="abs bottom-nav">Home<i>|</i>About Us<i>|</i>Services<i>|</i>Blog<i>|</i>Testimonials<i>|</i>Contact Us</div>
  <div class="abs copyright">Copyrights @ 2017 All Rights Reserved</div>
</footer>

</body>
</html>
```